CodeVarnaly.com Redesign

Please read the notes and see the site-map attached.
Updates

We are looking for something highly creative. Please provide your best work. Best of luck and thank you very much for your hard work!

Reason: I am seeing good designs but I am not seeing great designs. I really need a design that is unique and is going to wow me. No one is required to stick to the existing color schemes etc. You are free to use other colors etc. I am seeing a lot of the same colors that are used on the site now.

Target Market(s)

Business and entrepreneurs mainly. People looking to build applications, software or launch web or mobile tech products.

Colors

Designer to choose colors to be used in the design.

Requirements
Must have
• See my attached html file.
Nice to have
Should not have
• No sure

```html
<!DOCTYPE html>
<html lang="en">
<head>
<meta charset="utf-8">
<title>CodeVarnaly.com — Your Development Partner</title>
<link rel="stylesheet" href="https://fonts.googleapis.com/css2?family=Cabin:wght@400;500;600;700&family=Arimo:wght@400;700&display=swap">
<style>
:root{
  --navy:#1c4a78;
  --navy-dark:#163d66;
  --hero-blue:#1f5c98;
  --ink:#1f3a52;
  --text:#555b62;
  --muted:#8a9098;
  --green:#7bbf3a;
  --green-dark:#4f9a1e;
  --line:#d9dcdf;
  --white:#ffffff;
  --panel-top:#f4f4f4;
}
*{box-sizing:border-box;margin:0;padding:0}
html,body{width:1200px;height:1190px;overflow:hidden}
body{position:relative;background:var(--white);font-family:"Arimo",Arial,sans-serif;color:var(--text)}
.abs{position:absolute}

/* top bar */
.topbar{left:0;top:0;width:1200px;height:25px;background:var(--navy-dark);color:#e6edf5;font-family:"Cabin",sans-serif;font-size:11px}
.topbar .item{position:absolute;top:6px;display:flex;align-items:center;gap:6px}
.client-login{position:absolute;left:840px;top:2px;width:96px;height:21px;background:linear-gradient(#fff,#e6e6e6);border:1px solid #c9c9c9;border-radius:2px;color:#222;font-weight:700;font-size:9px;display:flex;align-items:center;justify-content:center;gap:5px}

/* header */
.brand{left:268px;top:34px;display:flex;align-items:center;gap:10px}
.brand-mark{width:36px;height:36px;border-radius:50%;background:var(--ink)}
.brand-name{font-family:"Cabin",sans-serif;font-weight:500;font-size:28px;color:var(--ink);letter-spacing:-.3px}
.search{left:556px;top:24px;width:382px;height:31px;border:1px solid var(--line);border-top:none;border-radius:0 0 4px 4px;background:#fff;display:flex;align-items:center;padding:0 9px;gap:14px;font-size:10px;color:#555}
.search .field{width:187px;height:20px;border:1px solid #ccc;border-radius:3px;background:linear-gradient(#f1f1f1,#fff);display:flex;justify-content:flex-end}
.search .go{width:76px;height:19px;margin-right:-1px;background:linear-gradient(#8fcf4a,var(--green-dark));border-radius:3px;color:#fff;font-family:"Cabin",sans-serif;font-weight:700;font-size:9px;letter-spacing:.5px;display:flex;align-items:center;justify-content:center}

.nav{left:263px;top:98px;width:675px;height:34px;background:linear-gradient(#fff,#e9e9e9);border:1px solid #d6d6d6;border-radius:3px 3px 5px 5px;display:flex;font-family:"Cabin",sans-serif;font-weight:600;font-size:11.5px;color:var(--ink)}
.nav a{display:flex;align-items:center;gap:6px;padding:0 9px;height:100%;border-right:1px solid #d2d2d2;text-decoration:none;color:inherit;position:relative}
.nav a.current::after{content:"";position:absolute;left:10px;right:8px;bottom:-1px;height:3px;background:var(--green)}

/* hero */
.hero{left:0;top:127px;width:1200px;height:233px;background:radial-gradient(ellipse 60% 90% at 50% 45%,#2a6fb0 0%,var(--hero-blue) 45%,#174c82 100%)}
.hero-title{left:306px;top:163px;font-family:"Cabin",sans-serif;font-weight:700;font-size:27px;color:#fff}
.hero-copy{left:309px;top:201px;width:318px;font-family:"Cabin",sans-serif;font-weight:700;font-size:13.4px;line-height:14px;color:#fff}
.hero-copy p+p{margin-top:13px}
.btn-green{background:linear-gradient(#9ad65a,var(--green) 50%,var(--green-dark));color:#fff;border-radius:16px;font-family:"Cabin",sans-serif;font-weight:700;display:flex;align-items:center;justify-content:center;box-shadow:0 1px 2px rgba(0,0,0,.3)}
.hero-btn{left:473px;top:298px;width:124px;height:32px;font-size:13px;letter-spacing:.5px}
.arrow{width:52px;height:52px;border-radius:50%;background:#fff;border:4px solid #0f2f52;display:flex;align-items:center;justify-content:center;box-shadow:0 0 0 2px rgba(255,255,255,.35)}
.hero-mark{left:726px;top:155px;width:100px;height:100px;border-radius:50%;background:#1a3550}
.hero-name{left:662px;top:298px;font-family:"Cabin",sans-serif;font-weight:500;font-size:40px;color:#1a3550;letter-spacing:-.5px}

/* panels */
.panel{background:#fff;border:1px solid var(--line);border-radius:3px;box-shadow:0 0 2px rgba(0,0,0,.06)}
.h-section{font-family:"Cabin",sans-serif;font-weight:700;font-size:15px;color:var(--ink)}
.h-section .accent{color:var(--green)}
.services{left:263px;top:372px;width:675px;height:208px}
.services .intro{position:absolute;left:11px;top:40px;width:385px;font-size:9.5px;line-height:15px;color:#333}
.service{position:absolute;width:210px;display:flex;gap:7px}
.service svg{flex-shrink:0}
.service h3{font-family:"Cabin",sans-serif;font-weight:600;font-size:11px;color:var(--ink);letter-spacing:.2px;margin-bottom:3px;white-space:nowrap}
.service p{font-size:8.3px;line-height:11.5px;color:var(--muted)}
.services .divider{position:absolute;left:427px;top:14px;height:180px;border-left:1px dotted #bbb}
.who{position:absolute;left:442px;top:14px}
.logo-tile{position:absolute;width:101px;height:67px;border:2px solid #e4e6e8;display:flex;align-items:center;justify-content:center;font-family:"Cabin",sans-serif;font-weight:700;font-size:16px;color:var(--ink)}

.portfolio{left:263px;top:591px;width:422px;height:257px;overflow:hidden}
.panel-head{position:absolute;left:0;top:0;width:100%;height:34px;background:linear-gradient(var(--panel-top),#fff);border-bottom:1px dashed #ccc;display:flex;align-items:center;justify-content:space-between;padding:0 10px}
.btn-small{background:linear-gradient(#98d25a,var(--green-dark));border:1px solid #4f8c22;color:#fff;border-radius:3px;font-size:9px;padding:3px 8px}
.photo{position:absolute;left:10px;top:50px;width:153px;height:100px;border:3px solid #e6e6e6;background:linear-gradient(135deg,#c98a14,#f0b627 40%,#d49516 65%,#3f8a2a)}
.post{position:absolute;left:171px;top:47px;width:240px}
.post .date{font-size:8px;color:#777}
.post h4{font-size:9.6px;font-weight:700;color:#111;line-height:12px;margin:3px 0 2px}
.post p{font-size:9.4px;line-height:13.5px;color:#555}
.bullets{position:absolute;left:10px;top:163px;width:398px;list-style:none}
.bullets li{border-top:1px dashed #ccc;padding:5px 0 6px 15px;font-size:9.4px;font-weight:700;color:#111;line-height:12.5px;position:relative}
.bullets li::before{content:"••";position:absolute;left:1px;top:4px;color:var(--green-dark);font-size:9px;letter-spacing:-1px}

.testimonials{left:696px;top:591px;width:242px;height:257px;overflow:hidden}
.testimonials .panel-head{padding:0 7px}
.testimonials .title{font-family:"Cabin",sans-serif;font-weight:700;font-size:12px;color:#1e1e1e}
.testimonials .btn-small{font-size:7px;padding:3px 4px}
.quote{position:absolute;left:10px;width:222px;font-size:9.3px;line-height:13px;color:#555;padding-bottom:6px;border-bottom:1px dashed #ccc}
.quote small{display:block;font-size:7px;color:#8a8a8a;margin-top:3px}

/* footer */
.footer-band{left:0;top:861px;width:1200px;height:329px;background:radial-gradient(ellipse 55% 70% at 50% 25%,#2a6ca8 0%,#1f5a92 45%,#1a4a7c 100%)}
.clients{left:263px;top:876px;width:675px;height:86px;background:linear-gradient(#fff,#f5f5f5);border-radius:2px}
.clients h2{position:absolute;left:0;width:100%;top:3px;text-align:center;font-family:"Cabin",sans-serif;font-weight:600;font-size:20px;color:#222;letter-spacing:.5px}
.clients .rule{position:absolute;left:8px;right:8px;top:31px;border-top:1px dashed #bbb}
.clients .row{position:absolute;left:12px;right:12px;top:42px;height:30px;display:flex;justify-content:space-between;align-items:center;font-family:"Cabin",sans-serif;font-weight:700;font-size:15px;color:#555}
.legal{left:764px;top:979px;width:174px;text-align:right;font-family:"Cabin",sans-serif;font-weight:700;font-size:9.6px;color:#fff;letter-spacing:.3px}
.footer-rule{left:263px;top:1005px;width:675px;border-top:1px solid #3d6f9e}
.footer-nav{left:263px;top:1024px;width:675px;display:flex;justify-content:space-between;font-family:"Arimo",sans-serif;font-weight:700;font-size:9.6px;color:#fff}
.footer-nav .sep{color:#c9d6e3}
.copyright{left:263px;top:1047px;width:675px;text-align:center;font-size:8.5px;color:#3b6b99}
</style>
</head>
<body>

<div class="abs topbar">
  <div class="item" style="left:276px">
    <svg width="15" height="11" viewBox="0 0 15 11"><rect x="0.5" y="0.5" width="14" height="10" fill="#fff"/><path d="M1 1l6.5 5L14 1" fill="none" stroke="#163d66" stroke-width="1.2"/></svg>
    reachus@codevarnaly.com
  </div>
  <div class="item" style="left:428px">
    <svg width="10" height="12" viewBox="0 0 10 12"><path d="M2 0h3l1 3-2 1.5c.6 1.6 1.5 2.7 3 3.4L8.5 6 10 9l-1 3C4 11 0 6 0 1z" fill="#fff"/></svg>
    +1 (555) 014-2290
  </div>
  <div class="item" style="left:653px">
    CHOOSE LANGUAGE:
    <svg width="17" height="11" viewBox="0 0 17 11"><rect width="17" height="11" fill="#fff"/><g fill="#c62b2b"><rect y="0" width="17" height="1.6"/><rect y="3.2" width="17" height="1.6"/><rect y="6.4" width="17" height="1.6"/><rect y="9.4" width="17" height="1.6"/></g><rect width="7" height="6" fill="#2a3f8f"/></svg>
    ENGLISH
    <svg width="8" height="5" viewBox="0 0 8 5" style="margin-left:6px"><path d="M0 0h8L4 5z" fill="#fff"/></svg>
  </div>
  <div class="client-login">
    <svg width="10" height="12" viewBox="0 0 10 12"><path d="M5 0l5 2v4c0 3-2.5 5-5 6C2.5 11 0 9 0 6V2z" fill="#4f9a1e"/><path d="M2.5 6l2 2 3-4" fill="none" stroke="#fff" stroke-width="1.3"/></svg>
    CLIENT LOGIN
  </div>
</div>

<div class="abs brand">
  <span class="brand-mark"></span>
  <span class="brand-name">codevarnaly</span>
</div>

<form class="abs search" role="search">
  <span>Search this website</span>
  <span class="field"><span class="go">SEARCH</span></span>
</form>

<nav class="abs nav">
  <a class="current" href="#">
    <svg width="20" height="18" viewBox="0 0 20 18"><path d="M10 1L1 9h3v8h5v-5h2v5h5V9h3z" fill="#2b4f6d"/></svg>Home</a>
  <a href="#" style="padding-left:13px">
    <svg width="26" height="18" viewBox="0 0 26 18"><circle cx="9" cy="5" r="4" fill="#2b4f6d"/><path d="M1 18c0-6 3-8 8-8s8 2 8 8z" fill="#2b4f6d"/><circle cx="18" cy="5" r="3.5" fill="#4a6f8e"/><path d="M14 11c2-1 3-1 5-1 4 0 6 2 6 8h-6" fill="#4a6f8e"/></svg>About Us</a>
  <a href="#" style="padding-left:13px">
    <svg width="22" height="18" viewBox="0 0 22 18"><rect x="1" y="4" width="20" height="13" rx="2" fill="none" stroke="#2b4f6d" stroke-width="2"/><path d="M7 4V1h8v3" fill="none" stroke="#2b4f6d" stroke-width="2"/><rect x="5" y="8" width="12" height="4" fill="#2b4f6d"/></svg>Our Work</a>
  <a href="#" style="padding-left:6px">
    <svg width="20" height="20" viewBox="0 0 20 20"><circle cx="10" cy="10" r="8.5" fill="none" stroke="#2b4f6d" stroke-width="2"/><path d="M3 7h14M3 13h14M10 1.5c-4 5-4 12 0 17M10 1.5c4 5 4 12 0 17" fill="none" stroke="#2b4f6d" stroke-width="1.5"/></svg>Services</a>
  <a href="#" style="padding-left:6px">
    <svg width="20" height="20" viewBox="0 0 20 20"><circle cx="10" cy="10" r="9.5" fill="#2b4f6d"/><path d="M10 4v8M6 9l4 4 4-4" fill="none" stroke="#fff" stroke-width="2"/></svg>Reach Us</a>
</nav>

<section class="abs hero"></section>
<h1 class="abs hero-title">Your Development Partner.</h1>
<div class="abs hero-copy">
  <p>We develop creative websites, web applications, mobile apps and custom applications that elicit smiles, create surprise and deliver more than expected.</p>
  <p>From vision to production. CodeVarnaly can help.</p>
</div>
<a class="abs btn-green hero-btn">More Services</a>
<div class="abs arrow" style="left:240px;top:211px">
  <svg width="20" height="22" viewBox="0 0 20 22"><path d="M15 2L5 11l10 9" fill="none" stroke="#6db33f" stroke-width="5"/></svg>
</div>
<div class="abs arrow" style="left:908px;top:211px">
  <svg width="20" height="22" viewBox="0 0 20 22"><path d="M5 2l10 9-10 9" fill="none" stroke="#6db33f" stroke-width="5"/></svg>
</div>
<span class="abs hero-mark"></span>
<span class="abs hero-name">codevarnaly</span>

<section class="abs panel services">
  <h2 class="h-section" style="position:absolute;left:11px;top:14px"><span class="accent">OUR</span> SERVICES</h2>
  <p class="intro">At vero eos et accusamus et iusto odio dignissimos ducimus blanditiis praesentium voluptatum deleniti atque corrupti quos dolores et quas.</p>

  <div class="service" style="left:4px;top:80px">
    <svg width="40" height="34" viewBox="0 0 40 34"><circle cx="13" cy="19" r="9" fill="none" stroke="#2b4f6d" stroke-width="6" stroke-dasharray="4 3"/><circle cx="13" cy="19" r="5" fill="#2b4f6d"/><path d="M18 26L35 6l4 3-17 20-6 2z" fill="#7bbf3a"/></svg>
    <div><h3>WEB DEVELOPMENT</h3><p>Lorem ipsum dolor sit amet, consectetur adipisicing elit, sed do eiusmod tempor incididunt ut labore et dolore magna</p></div>
  </div>
  <div class="service" style="left:216px;top:80px">
    <svg width="34" height="32" viewBox="0 0 34 32"><path d="M4 4l4-3 22 25-4 4z" fill="#2b4f6d"/><path d="M30 2a6 6 0 0 0-7 8L4 27l3 3 17-19a6 6 0 0 0 8-7l-3 3-3-1-1-3z" fill="#2b4f6d"/></svg>
    <div><h3>SOFTWARE DEVELOPMENT</h3><p>Sed do eiusmod tempor incididunt ut labore et dolore magna aliqua. Ut enim ad minim veniam, quis nostrud exercitation</p></div>
  </div>
  <div class="service" style="left:9px;top:136px">
    <svg width="30" height="40" viewBox="0 0 30 40"><rect x="2" y="6" width="18" height="32" rx="3" fill="none" stroke="#2b4f6d" stroke-width="3"/><rect x="6" y="11" width="10" height="20" fill="#7bbf3a"/><circle cx="11" cy="34" r="1.5" fill="#2b4f6d"/><path d="M22 8a6 6 0 0 1 4-6M23 11a10 10 0 0 1 6-9" fill="none" stroke="#7bbf3a" stroke-width="2"/></svg>
    <div><h3>MOBILE APP DEVELOPMENT</h3><p>Eiusmod tempor incididunt ut labore et dolore magna aliqua. Ut enim ad minim veniam, quis nostrud exercitation</p></div>
  </div>
  <div class="service" style="left:220px;top:136px">
    <svg width="30" height="40" viewBox="0 0 30 40"><rect x="2" y="3" width="26" height="36" rx="2" fill="none" stroke="#2b4f6d" stroke-width="2.5"/><rect x="10" y="0" width="10" height="6" fill="#2b4f6d"/><circle cx="15" cy="15" r="4" fill="#7bbf3a"/><path d="M8 27c0-5 3-7 7-7s7 2 7 7z" fill="#7bbf3a"/><rect x="7" y="30" width="16" height="2" fill="#2b4f6d"/><rect x="7" y="34" width="16" height="2" fill="#2b4f6d"/></svg>
    <div><h3>USER EXPERIENCE DESIGN</h3><p>Quis nostrud exercitation ullamco laboris nisi ut aliquip ex ea commodo consequat. Duis aute irure dolor in reprehenderit in</p></div>
  </div>

  <span class="divider"></span>
  <div class="who">
    <h2 class="h-section">WHO <span class="accent">WE</span> <span style="color:#8a9aa8">ARE</span></h2>
  </div>
  <div class="logo-tile" style="left:422px;top:44px">Quorvane</div>
  <div class="logo-tile" style="left:528px;top:44px">Trenvalo</div>
  <div class="logo-tile" style="left:422px;top:119px">Durnexa</div>
  <div class="logo-tile" style="left:528px;top:119px">Kelmoray</div>
</section>

<section class="abs panel portfolio">
  <div class="panel-head">
    <h2 style="font-family:'Cabin',sans-serif;font-weight:700;font-size:20px;color:var(--ink)"><span style="color:var(--green)">Our</span> Portfolio</h2>
    <span class="btn-small">Visit More Work</span>
  </div>
  <div class="photo" role="img" aria-label="Close-up photo of yellow and green toy building bricks"></div>
  <article class="post">
    <div class="date">25th March 2014</div>
    <h4>Lorem ipsum dolor sit amet, consectetur adipisicing elit, sed do eiusmod.</h4>
    <p>Lorem ipsum dolor sit amet, consectetur adipisicing elit, sed do eiusmod tempor incididunt ut labore et dolore magna aliqua. Ut enim ad minim veniam, quis nostrud exercitation ullamco laboris nisi ut aliquip ex ea commo-do consequat.</p>
  </article>
  <ul class="bullets">
    <li>Lorem ipsum dolor sit amet, consectetur adipisicing elit, sed do eiusmod.</li>
    <li>Tempor incididunt ut labore et dolore magna aliqua. Ut enim ad minim veniam.</li>
    <li>Ruis nostrud exercitation ullamco laboris nisi ut aliquip ex ea commodo consequat. Duis aute irure dolor in reprehenderit in voluptate velit esse.</li>
  </ul>
</section>

<section class="abs panel testimonials">
  <div class="panel-head">
    <h2 class="title">WHY CLIENTS LOVE US!</h2>
    <span class="btn-small">More testimonials</span>
  </div>
  <div class="quote" style="top:45px">Lorem ipsum dolor sit amet, consectetur adipisicing elit, sed do eiusmod tempor<small>about 1 hour ago reply</small></div>
  <div class="quote" style="top:98px">Lorem ipsum dolor sit amet, consectetur adipisicing elit, sed do eiusmod tempor<small>about 1 hour ago reply</small></div>
  <div class="quote" style="top:151px">Lorem ipsum dolor sit amet, consectetur adipisicing elit, sed do eiusmod tempor<small>about 1 hour ago reply</small></div>
  <div class="quote" style="top:204px;border-bottom:none">Lorem ipsum dolor sit amet, consectetur adipisicing elit, sed do eiusmod tempor<small>about 1 hour ago reply</small></div>
</section>

<footer>
  <div class="abs footer-band"></div>
  <section class="abs clients">
    <h2>Our Clients</h2>
    <span class="rule"></span>
    <div class="row">
      <span>Plazivo</span><span>Vostrelle</span><span>Felnaxo</span><span>Obrenti</span><span>Sarquell</span><span>Ninvora</span><span>Holvexa</span>
    </div>
  </section>
  <div class="abs legal">Terms of Services | Privacy Policy</div>
  <div class="abs footer-rule"></div>
  <nav class="abs footer-nav">
    <span>HOME</span><span class="sep">|</span><span>THE ORGNIZATION</span><span class="sep">|</span><span>OUR OPERATIONS</span><span class="sep">|</span><span>NEWS &amp; EVENTS</span><span class="sep">|</span><span>SPONSORS</span><span class="sep">|</span><span>COMMUNITY</span><span class="sep">|</span><span>BLOG</span><span class="sep">|</span><span>CONTACT US</span>
  </nav>
  <div class="abs copyright">Copyright 2014, All Rights Reserved.</div>
</footer>

</body>
</html>
```